Business cards and stationery for a software company
Klovarent s.r.o.
Simple
Petr Hrubeš
Lipová alej 2841/9
Praha 5
petr.hrubes@klovarent-example.com
www.klovarent-example.com

```html
<!DOCTYPE html>
<html lang="cs">
<head>
<meta charset="utf-8">
<title>Klovarent – vizitky</title>
<link rel="stylesheet" href="https://fonts.googleapis.com/css2?family=Open+Sans:wght@400;600;700&display=swap">
<style>
  :root {
    --page-bg: #e9e7e4;
    --band-dark-top: #3a4a55;
    --band-dark-bottom: #1b242b;
    --card-white: #fbfbfb;
    --card-grey: #e6e6e6;
    --ink: #3b3b3b;
    --ink-soft: #555a60;
    --name-ink: #5b5f78;
    --accent: #7a4f9a;
    --accent-light: #a27cc2;
    --black-band: #141414;
  }
  * { margin: 0; padding: 0; box-sizing: border-box; }
  html, body { width: 1200px; height: 896px; overflow: hidden; }
  body {
    background: var(--page-bg);
    font-family: "Open Sans", Arial, sans-serif;
    position: relative;
  }
  .card {
    position: absolute;
    width: 560px;
    height: 311px;
    background: linear-gradient(180deg, var(--card-white) 0%, var(--card-grey) 100%);
    box-shadow: 0 8px 24px rgba(0,0,0,0.25);
    overflow: hidden;
  }
  .card--front { left: 60px; top: 70px; }
  .card--back { left: 580px; top: 510px; }

  .front-band {
    height: 178px;
    background: linear-gradient(180deg, var(--band-dark-top) 0%, var(--band-dark-bottom) 100%);
    display: flex;
    align-items: center;
    justify-content: center;
  }
  .brand {
    display: flex;
    align-items: center;
    gap: 12px;
    font-weight: 700;
    letter-spacing: -0.5px;
  }
  .brand__dot {
    width: 30px; height: 30px;
    border-radius: 50%;
    background: var(--accent-light);
  }
  .brand--light { color: #ffffff; font-size: 38px; }
  .brand--dark { color: var(--ink); font-size: 42px; }
  .brand--dark .brand__dot { background: var(--accent); width: 34px; height: 34px; }

  .front-body {
    position: relative;
    height: 133px;
  }
  .person-name {
    position: absolute;
    left: 40px; top: 18px;
    font-size: 21px;
    font-weight: 700;
    color: var(--name-ink);
  }
  .contacts {
    position: absolute;
    left: 318px; top: 14px;
    list-style: none;
    font-size: 12px;
    color: var(--ink-soft);
    line-height: 1.25;
  }
  .contacts li {
    display: flex;
    align-items: flex-start;
    gap: 7px;
    margin-bottom: 6px;
  }
  .contacts svg { flex: none; margin-top: 1px; }
  .contacts .street { margin-bottom: 0; }

  .back-band {
    position: absolute;
    left: 0; bottom: 0;
  }
  .back-logo {
    position: absolute;
    left: 0; right: 0; top: 110px;
    display: flex;
    justify-content: center;
  }
</style>
</head>
<body>

<section class="card card--front" aria-label="Vizitka – přední strana">
  <div class="front-band">
    <div class="brand brand--light"><span class="brand__dot"></span>Klovarent</div>
  </div>
  <div class="front-body">
    <h1 class="person-name">Petr Hrubeš</h1>
    <ul class="contacts">
      <li class="street">
        <svg width="13" height="13" viewBox="0 0 13 13"><circle cx="6.5" cy="6.5" r="6.5" fill="var(--accent)"/><path d="M3 6.8 6.5 3.5 10 6.8M4.2 6.2V9.8H8.8V6.2" fill="none" stroke="#fff" stroke-width="1.1"/></svg>
        <span>Lipová alej 2841/9<br>Praha 5</span>
      </li>
      <li>
        <svg width="13" height="13" viewBox="0 0 13 13"><circle cx="6.5" cy="6.5" r="6.5" fill="var(--accent)"/><path d="M4.3 3.6c.5-.4 1-.3 1.2.2l.5 1.1c.1.4-.1.6-.4.9.4.8 1 1.4 1.8 1.8.3-.3.5-.5.9-.4l1.1.5c.5.2.6.7.2 1.2-.9 1-2.5.5-4-1s-2.2-3.2-1.3-4.3z" fill="#fff"/></svg>
        <span>+420 601 555 274</span>
      </li>
      <li>
        <svg width="13" height="13" viewBox="0 0 13 13"><circle cx="6.5" cy="6.5" r="6.5" fill="var(--accent)"/><rect x="3.3" y="4.3" width="6.4" height="4.4" fill="none" stroke="#fff" stroke-width="1"/><path d="M3.3 4.3 6.5 6.8 9.7 4.3" fill="none" stroke="#fff" stroke-width="1"/></svg>
        <span>petr.hrubes@klovarent-example.com</span>
      </li>
      <li>
        <svg width="13" height="13" viewBox="0 0 13 13"><circle cx="6.5" cy="6.5" r="6.5" fill="var(--accent)"/><circle cx="6.5" cy="6.5" r="3.3" fill="none" stroke="#fff" stroke-width="1"/><path d="M3.2 6.5h6.6M6.5 3.2c-1.4 1.8-1.4 4.8 0 6.6M6.5 3.2c1.4 1.8 1.4 4.8 0 6.6" fill="none" stroke="#fff" stroke-width=".8"/></svg>
        <span>www.klovarent-example.com</span>
      </li>
    </ul>
  </div>
</section>

<section class="card card--back" aria-label="Vizitka – zadní strana">
  <div class="back-logo">
    <div class="brand brand--dark"><span class="brand__dot"></span>Klovarent</div>
  </div>
  <svg class="back-band" width="560" height="30" viewBox="0 0 560 30" aria-hidden="true">
    <defs>
      <linearGradient id="accentBand" x1="0" y1="0" x2="1" y2="0">
        <stop offset="0" stop-color="var(--accent-light)"/>
        <stop offset="1" stop-color="var(--accent)"/>
      </linearGradient>
    </defs>
    <polygon points="0,12 380,12 362,30 0,30" fill="url(#accentBand)"/>
    <polygon points="392,12 560,12 560,30 374,30" fill="var(--black-band)"/>
  </svg>
</section>

</body>
</html>
```